TEAL BEACON LICE REMOVAL labels

I need a label design for our MINT REPELLING SHAMPOO (LICE PREVENTION).
It also includes our MINT REPELLING CONDITIONER (LICE PREVENTION) and our MINT SPRAY (LICE PREVENTION) also includes LICE & NIT ELIMINATING MOUSSE (LICE TREATMENT) and a LICE ELIMINATOR 100% Dimethicone oil (LICE TREATMENT). The shampoo and conditioner are sulfate free, contains peppermint and other essential oils and is safe for the entire family. Label should be simple, modern and high end looking. Fun is good too if it looks nice!

Target Market(s)

Kids and Adults

Industry/Entity Type

Hair Care Product

Font styles to use
Sans Serif
Decorative

Requirements
Must have
• -Words that should be used: safe, non toxic, sulfate free, essential oils, pesticide free. - Naturally removes lice, super lice & nits are great words for the lice & nit eliminating mousse and treatment oil 100% Dimethicone oil
- On a side note there are no essential oils in the lice & nit eliminating mousse or treatment oil 100% Dimethicone oil
Nice to have
• Earth tone colors if possible
Kid safe, no fillers, colors or scents
100% effective (even against super lice)
8oz labels and 4oz labels
Should not have
• No pictures of lice

```html
<!DOCTYPE html>
<html lang="en">
<head>
<meta charset="utf-8">
<title>Teal Beacon Lice Removal – Label Range</title>
<link href="https://fonts.googleapis.com/css2?family=Playfair+Display:wght@700&family=Hind:wght@400;600&display=swap" rel="stylesheet">
<style>
  :root {
    --page: #ffffff;
    --label: #fdfdfb;
    --leaf-light: #eef4e4;
    --leaf-mid: #e2ecd4;
    --accent: #dc5520;
    --ink: #222222;
    --edge: #e6e6e0;
  }
  * { box-sizing: border-box; margin: 0; padding: 0; }
  html, body {
    width: 1200px; height: 1120px; overflow: hidden;
    background: var(--page);
  }
  .range {
    width: 1200px; height: 1120px;
    display: flex; align-items: center; justify-content: center;
    gap: 18px;
  }
  .label {
    position: relative;
    width: 218px; height: 780px;
    background: var(--label);
    border: 1px solid var(--edge);
    border-radius: 6px;
    overflow: hidden;
    display: flex; flex-direction: column; align-items: center;
    padding: 56px 14px 34px;
    text-align: center;
  }
  .label--small { height: 600px; padding-top: 40px; }
  .leaf-pattern {
    position: absolute; inset: 0;
    background: linear-gradient(160deg, var(--leaf-light) 0%, var(--label) 45%, var(--leaf-mid) 100%);
    z-index: 0;
  }
  .label > *:not(.leaf-pattern) { position: relative; z-index: 1; }
  .brand {
    display: flex; align-items: center; gap: 8px;
    margin-bottom: 44px;
  }
  .brand-dot {
    width: 18px; height: 18px; border-radius: 50%;
    background: var(--accent); flex: none;
  }
  .brand-name {
    font-family: "Hind", sans-serif; font-weight: 600;
    font-size: 13px; letter-spacing: 2.5px; line-height: 1.35;
    color: var(--ink); text-align: left;
  }
  .product-name {
    font-family: "Playfair Display", serif; font-weight: 700;
    color: var(--accent);
    font-size: 26px; line-height: 1.04; text-transform: uppercase;
    letter-spacing: -0.5px;
  }
  .formula {
    font-family: "Playfair Display", serif; font-weight: 700;
    color: var(--accent); font-size: 16px; margin-top: 6px;
  }
  .purpose {
    font-family: "Hind", sans-serif; font-weight: 600;
    font-size: 14px; letter-spacing: 0.4px;
    color: var(--ink); margin-top: 14px;
  }
  .purpose--treatment { color: var(--accent); }
  .claims {
    font-family: "Hind", sans-serif; font-weight: 400;
    font-size: 13.5px; line-height: 1.4; color: var(--ink);
    margin-top: 18px;
  }
  .volume {
    margin-top: auto;
    font-family: "Playfair Display", serif; font-weight: 700;
    font-size: 13px; color: var(--ink);
  }
  .volume span { font-weight: 400; padding: 0 4px; }
</style>
</head>
<body>
<main class="range">

  <section class="label label--small">
    <div class="leaf-pattern" role="img" aria-label="Soft pale green peppermint leaf line pattern"></div>
    <div class="brand"><span class="brand-dot"></span><span class="brand-name">TEAL BEACON<br>LICE REMOVAL</span></div>
    <h2 class="product-name">Lice<br>Eliminator</h2>
    <p class="formula">100% Dimethicone Oil</p>
    <p class="purpose purpose--treatment">(LICE TREATMENT)</p>
    <p class="claims">Naturally removes lice,<br>super lice &amp; nits.<br>Sulfate free, non toxic,<br>pesticide free and safe<br>for the entire family</p>
    <p class="volume">4oz<span>|</span>118ml</p>
  </section>

  <section class="label">
    <div class="leaf-pattern" role="img" aria-label="Soft pale green peppermint leaf line pattern"></div>
    <div class="brand"><span class="brand-dot"></span><span class="brand-name">TEAL BEACON<br>LICE REMOVAL</span></div>
    <h2 class="product-name">Mint Spray</h2>
    <p class="purpose">(LICE PREVENTION)</p>
    <p class="claims">Sulfate free, non toxic,<br>pesticide free,<br>contains peppermint,<br>essential oils<br>and is safe for the<br>entire family</p>
    <p class="volume">8oz<span>|</span>236ml</p>
  </section>

  <section class="label">
    <div class="leaf-pattern" role="img" aria-label="Soft pale green peppermint leaf line pattern"></div>
    <div class="brand"><span class="brand-dot"></span><span class="brand-name">TEAL BEACON<br>LICE REMOVAL</span></div>
    <h2 class="product-name">Mint<br>Repelling<br>Shampoo</h2>
    <p class="purpose">(LICE PREVENTION)</p>
    <p class="claims">Sulfate free, non toxic,<br>pesticide free,<br>contains peppermint,<br>essential oils<br>and is safe for the<br>entire family</p>
    <p class="volume">8oz<span>|</span>236ml</p>
  </section>

  <section class="label">
    <div class="leaf-pattern" role="img" aria-label="Soft pale green peppermint leaf line pattern"></div>
    <div class="brand"><span class="brand-dot"></span><span class="brand-name">TEAL BEACON<br>LICE REMOVAL</span></div>
    <h2 class="product-name">Lice &amp; Nit<br>Eliminating<br>Mousse</h2>
    <p class="formula">100% Dimethicone Oil</p>
    <p class="purpose purpose--treatment">(LICE TREATMENT)</p>
    <p class="claims">Naturally removes lice,<br>super lice &amp; nits.<br>Sulfate free, non toxic,<br>pesticide free and safe<br>for the entire family</p>
    <p class="volume">8oz<span>|</span>236ml</p>
  </section>

  <section class="label">
    <div class="leaf-pattern" role="img" aria-label="Soft pale green peppermint leaf line pattern"></div>
    <div class="brand"><span class="brand-dot"></span><span class="brand-name">TEAL BEACON<br>LICE REMOVAL</span></div>
    <h2 class="product-name">Mint<br>Repelling<br>Conditioner</h2>
    <p class="purpose">(LICE PREVENTION)</p>
    <p class="claims">Sulfate free, non toxic,<br>pesticide free,<br>contains peppermint,<br>essential oils<br>and is safe for the<br>entire family</p>
    <p class="volume">8oz<span>|</span>236ml</p>
  </section>

</main>
</body>
</html>
```